Essential Oil 15ml - package of 6

Design of a box of 6 different essential oils.
+ design of the bottle stickers
My bottles are 15ml clear blue glass.

The pictures attached are my competitors...

Target Market(s)

BRAMBLEWICK USA

Font styles to use
Serif

Requirements
Must have
• Our logo + "essential oil" and type (lavender, eucalyptus etc....)
• 15ml - 0.50 fl.oz.
• special color for the oil type.

```html
<!DOCTYPE html>
<html lang="en">
<head>
<meta charset="UTF-8">
<title>Tamar Grove – Lavender Essential Oil Label</title>
<link href="https://fonts.googleapis.com/css2?family=Cinzel:wght@500&family=Marcellus&family=Open+Sans:ital,wght@0,400;1,400&display=swap" rel="stylesheet">
<style>
  :root {
    --page-bg: #ffffff;
    --lavender: #a48bc0;
    --label-dark: #3b3a3c;
    --label-dark-edge: #2c2b2d;
    --gold: #877a28;
    --rule-light: #b9b6bd;
    --title-white: #f4f2f6;
    --body-grey: #dcd6e4;
    --small-lilac: #b8a6cf;
  }
  html, body {
    margin: 0;
    padding: 0;
    width: 1200px;
    height: 1000px;
    overflow: hidden;
    background: var(--page-bg);
  }
  .canvas {
    position: relative;
    width: 1200px;
    height: 1000px;
  }
  .bottle-label {
    position: absolute;
    left: 330px;
    top: 50px;
    width: 540px;
    height: 900px;
    display: block;
  }
  .label-body { fill: url(#bodyShade); }
  .label-band { fill: var(--lavender); }
  .label-rule { stroke: var(--rule-light); stroke-width: 2; }
  .brand-mark { fill: var(--gold); }
  .brand-name {
    font-family: "Marcellus", serif;
    font-size: 58px;
    fill: var(--gold);
  }
  .oil-type {
    font-family: "Cinzel", serif;
    font-weight: 500;
    font-size: 76px;
    letter-spacing: 1px;
    fill: var(--title-white);
  }
  .title-rule { stroke: var(--gold); stroke-width: 2; }
  .oil-claim {
    font-family: "Open Sans", sans-serif;
    font-size: 27px;
    fill: var(--body-grey);
  }
  .oil-description {
    font-family: "Open Sans", sans-serif;
    font-style: italic;
    font-size: 19px;
    fill: var(--small-lilac);
  }
  .oil-volume {
    font-family: "Marcellus", serif;
    font-size: 40px;
    fill: var(--gold);
  }
</style>
</head>
<body>
<main class="canvas">
  <svg class="bottle-label" viewBox="0 0 540 900" xmlns="http://www.w3.org/2000/svg" aria-label="Tamar Grove lavender essential oil bottle label">
    <defs>
      <linearGradient id="bodyShade" x1="0" x2="1" y1="0" y2="0">
        <stop offset="0" stop-color="var(--label-dark-edge)"/>
        <stop offset="0.5" stop-color="var(--label-dark)"/>
        <stop offset="1" stop-color="var(--label-dark-edge)"/>
      </linearGradient>
    </defs>

    <rect class="label-body" x="0" y="0" width="540" height="900"/>

    <path class="label-band top-band"
          d="M0,0 H540 V132 H462 V363 Q462,407 418,407 H121 Q77,407 77,363 V132 H0 Z"/>
    <path class="label-band bottom-band"
          d="M0,825 H176 V788 Q176,744 220,744 H319 Q363,744 363,788 V825 H540 V900 H0 Z"/>

    <g class="top-rules">
      <line class="label-rule" x1="0" y1="142" x2="77" y2="142"/>
      <line class="label-rule" x1="0" y1="149" x2="77" y2="149"/>
      <line class="label-rule" x1="462" y1="142" x2="540" y2="142"/>
      <line class="label-rule" x1="462" y1="149" x2="540" y2="149"/>
    </g>
    <g class="bottom-rules">
      <line class="label-rule" x1="0" y1="808" x2="176" y2="808"/>
      <line class="label-rule" x1="0" y1="815" x2="176" y2="815"/>
      <line class="label-rule" x1="363" y1="808" x2="540" y2="808"/>
      <line class="label-rule" x1="363" y1="815" x2="540" y2="815"/>
    </g>

    <circle class="brand-mark" cx="270" cy="215" r="40"/>
    <text class="brand-name" x="270" y="325" text-anchor="middle">Tamar Grove</text>

    <text class="oil-type" x="270" y="520" text-anchor="middle">LAVENDER</text>
    <line class="title-rule" x1="138" y1="558" x2="402" y2="558"/>
    <text class="oil-claim" x="270" y="605" text-anchor="middle">100% Pure Essential Oils</text>

    <text class="oil-description" text-anchor="middle">
      <tspan x="270" y="655">Lorem ipsum dolor sit amet, in inermis aliquando</tspan>
      <tspan x="270" y="682">vix, an eam utinam integre reformidans. Persecuti</tspan>
      <tspan x="270" y="709">contentiones ex vim.</tspan>
    </text>

    <text class="oil-volume" x="270" y="800" text-anchor="middle">15 ml</text>
  </svg>
</main>
</body>
</html>
```